Events Calendar and Event Reminder Postcard Design

We need a Calendar of Events and an Event Reminder Postcard that utilize the same design look to create a uniform branding appearance. The design format for the 11" x 17" calendar page should be somewhat similar to the attached calendar sample, but not exactly the same. The 4.25" x 5.5" (4 up on an 8.5"x11" sheet) postcard needs to be able to accommodate the amount of information referenced in the attached example of our existing event reminder postcard. Our logo has been uploaded and should be included on both pieces as well. Prefer Adobe Illustrator files.
Updates

Project Deadline Extended
Reason: Many of the designs need further review

Target Market(s)

TVM Membership

Industry/Entity Type

Events

Font styles to use
Serif
Sans Serif

Requirements
Must have
• See Description and the attached sample files. Prefer Adobe InDesign files
Should not have
• Should not be cartoonish in nature

```html
<!DOCTYPE html>
<html lang="en">
<head>
<meta charset="utf-8">
<title>TVM 2017 Calendar of Events and Event Reminder Postcard</title>
<link href="https://fonts.googleapis.com/css2?family=Josefin+Sans:wght@300;400;600;700&family=Arimo:wght@400;700&display=swap" rel="stylesheet">
<style>
  :root {
    --bg: #efefef;
    --paper: #ffffff;
    --stone: #6b6660;
    --stone-dark: #5f5b56;
    --sage: #7b9e98;
    --rule: #a9a6a2;
    --ink: #3e3b38;
  }
  * { box-sizing: border-box; margin: 0; padding: 0; }
  html, body { width: 1200px; height: 1000px; overflow: hidden; }
  body { background: var(--bg); position: relative; font-family: "Josefin Sans", sans-serif; color: var(--stone); }

  /* ---------- Calendar sheet ---------- */
  .calendar-sheet {
    position: absolute; left: 122px; top: 30px; width: 610px; height: 940px;
    background: var(--paper);
  }
  .brand-mark {
    position: absolute; left: 78px; top: 78px;
    display: flex; align-items: center; gap: 14px;
  }
  .brand-mark .brand-square { width: 26px; height: 26px; background: var(--stone); }
  .brand-mark .brand-name {
    font-size: 92px; font-weight: 700; color: var(--stone); line-height: 1; letter-spacing: 2px;
    padding-top: 14px;
  }
  .sheet-title { position: absolute; left: 346px; top: 40px; width: 200px; text-align: center; }
  .sheet-title .year { font-size: 66px; font-weight: 300; color: var(--sage); line-height: 1; letter-spacing: 2px; }
  .sheet-title .heading { font-size: 32px; font-weight: 300; color: var(--stone); line-height: 44px; letter-spacing: 1px; margin-top: 2px; }

  .month-column { position: absolute; top: 226px; width: 192px; }
  .month-column.col-1 { left: 8px; }
  .month-column.col-2 { left: 218px; }
  .month-column.col-3 { left: 415px; }

  .month-name {
    height: 28px; margin-top: 8px; font-size: 20px; font-weight: 700; color: var(--stone);
    line-height: 28px; letter-spacing: 0.3px;
  }
  .month-name:first-child { margin-top: 0; }

  .event { display: flex; height: 52px; align-items: flex-start; }
  .event .day {
    width: 51px; font-size: 33px; font-weight: 300; color: var(--sage); line-height: 1; padding-top: 6px;
  }
  .event .details {
    border-left: 1px solid var(--rule); padding-left: 5px; min-height: 42px;
    font-family: "Arimo", sans-serif; font-size: 7.4px; line-height: 9.6px; color: var(--ink); width: 136px;
  }
  .event .details strong { font-weight: 700; }

  .sheet-footer {
    position: absolute; left: 0; bottom: 0; width: 610px; height: 14px; background: var(--stone-dark);
    color: #fff; font-family: "Arimo", sans-serif; font-weight: 700; font-size: 7.4px; line-height: 14px; padding-left: 9px;
  }

  /* ---------- Reminder postcard ---------- */
  .reminder-card {
    position: absolute; left: 793px; top: 181px; width: 284px; height: 219px;
    background: var(--paper); border: 1px solid #dcdcdc;
  }
  .reminder-card .card-brand {
    position: absolute; left: 14px; top: 26px; display: flex; align-items: center; gap: 6px;
  }
  .reminder-card .card-brand .brand-square { width: 10px; height: 10px; background: var(--stone); }
  .reminder-card .card-brand .brand-name { font-size: 34px; font-weight: 700; color: var(--stone); line-height: 1; padding-top: 6px; }
  .reminder-card .card-headline {
    position: absolute; left: 118px; top: 11px; width: 160px;
    font-family: "Arimo", sans-serif; font-weight: 700; font-size: 12.6px; line-height: 18.5px; color: var(--stone);
  }
  .reminder-card .card-body {
    position: absolute; left: 12px; top: 96px; width: 165px;
    font-family: "Arimo", sans-serif; font-size: 5.2px; line-height: 6.9px; color: var(--ink);
  }
  .reminder-card .partner-name {
    position: absolute; left: 186px; top: 104px;
    font-family: "Arimo", sans-serif; font-weight: 700; font-size: 20px; color: var(--stone); letter-spacing: -0.5px;
  }
  .reminder-card .call-line {
    position: absolute; left: 12px; top: 163px;
    font-family: "Arimo", sans-serif; font-weight: 700; font-size: 11.4px; color: var(--sage);
  }
  .reminder-card .online-line {
    position: absolute; left: 82px; top: 180px;
    font-family: "Arimo", sans-serif; font-size: 7px; color: var(--ink);
  }
  .reminder-card .web-line {
    position: absolute; left: 12px; top: 194px;
    font-family: "Arimo", sans-serif; font-weight: 700; font-size: 9.4px; color: var(--sage);
  }
  .reminder-card .card-band {
    position: absolute; left: -1px; bottom: -1px; width: 284px; height: 7px; background: var(--stone-dark);
  }
</style>
</head>
<body>

<section class="calendar-sheet" aria-label="2017 Calendar of Events">
  <div class="brand-mark">
    <span class="brand-square"></span>
    <span class="brand-name">TVM</span>
  </div>

  <header class="sheet-title">
    <div class="year">2017</div>
    <div class="heading">CALENDAR<br>OF EVENTS</div>
  </header>

  <div class="month-column col-1">
    <h2 class="month-name">JANUARY</h2>
    <div class="event"><span class="day">02</span><p class="details"><strong>Lorem ipsum</strong> dolor sit amet, consectetur adipiscing elit, sed do eiusmod tempor incididunt ut labore et</p></div>
    <div class="event"><span class="day">12</span><p class="details"><strong>Lorem ipsum</strong> dolor sit amet, consectetur adipiscing elit, sed do eiusmod tempor incididunt ut labore et tetur adipiscing elit, sed do eiusmod</p></div>
    <div class="event"><span class="day">30</span><p class="details"><strong>Lorem ipsum</strong> dolor sit amet, consectetur adipiscing elit, sed do eiusmod tempor incididunt ut labore et tetur adipiscing elit, sed do eiusmod</p></div>
    <h2 class="month-name">FEBRUARY</h2>
    <div class="event"><span class="day">10</span><p class="details"><strong>Lorem ipsum</strong> dolor sit amet, consectetur adipiscing elit, sed do eiusmod tempor incididunt ut labore et</p></div>
    <div class="event"><span class="day">25</span><p class="details"><strong>Lorem ipsum</strong> dolor sit amet, consectetur adipiscing elit, sed do eiusmod tempor incididunt ut labore et tetur adipiscing elit, sed do eiusmod</p></div>
    <h2 class="month-name">MARCH</h2>
    <div class="event"><span class="day">08</span><p class="details"><strong>Lorem ipsum</strong> dolor sit amet, consectetur adipiscing elit, sed do eiusmod tempor incididunt ut labore et</p></div>
    <div class="event"><span class="day">19</span><p class="details"><strong>Lorem ipsum</strong> dolor sit amet, consectetur adipiscing elit, sed do eiusmod tempor incididunt ut labore et tetur adipiscing elit, sed do eiusmod</p></div>
    <div class="event"><span class="day">23</span><p class="details"><strong>Lorem ipsum</strong> dolor sit amet, consectetur adipiscing elit, sed do eiusmod tempor incididunt ut labore et tetur adipiscing elit, sed do eiusmod</p></div>
    <h2 class="month-name">APRIL</h2>
    <div class="event"><span class="day">03</span><p class="details"><strong>Lorem ipsum</strong> dolor sit amet, consectetur adipiscing elit, sed do eiusmod tempor incididunt ut labore et</p></div>
    <div class="event"><span class="day">13</span><p class="details"><strong>Lorem ipsum</strong> dolor sit amet, consectetur adipiscing elit, sed do eiusmod tempor incididunt ut labore et tetur adipiscing elit, sed do eiusmod</p></div>
  </div>

  <div class="month-column col-2">
    <h2 class="month-name">MAY</h2>
    <div class="event"><span class="day">01</span><p class="details"><strong>Lorem ipsum</strong> dolor sit amet, consectetur adipiscing elit, sed do eiusmod tempor incididunt ut labore et</p></div>
    <div class="event"><span class="day">23</span><p class="details"><strong>Lorem ipsum</strong> dolor sit amet, consectetur adipiscing elit, sed do eiusmod tempor incididunt ut labore et tetur adipiscing elit, sed do eiusmod</p></div>
    <h2 class="month-name">JUNE</h2>
    <div class="event"><span class="day">10</span><p class="details"><strong>Lorem ipsum</strong> dolor sit amet, consectetur adipiscing elit, sed do eiusmod tempor incididunt ut labore et</p></div>
    <div class="event"><span class="day">25</span><p class="details"><strong>Lorem ipsum</strong> dolor sit amet, consectetur adipiscing elit, sed do eiusmod tempor incididunt ut labore et tetur adipiscing elit, sed do eiusmod</p></div>
    <h2 class="month-name">JULY</h2>
    <div class="event"><span class="day">05</span><p class="details"><strong>Lorem ipsum</strong> dolor sit amet, consectetur adipiscing elit, sed do eiusmod tempor incididunt ut labore et</p></div>
    <div class="event"><span class="day">17</span><p class="details"><strong>Lorem ipsum</strong> dolor sit amet, consectetur adipiscing elit, sed do eiusmod tempor incididunt ut labore et tetur adipiscing elit, sed do eiusmod</p></div>
    <div class="event"><span class="day">22</span><p class="details"><strong>Lorem ipsum</strong> dolor sit amet, consectetur adipiscing elit, sed do eiusmod tempor incididunt ut labore et tetur adipiscing elit, sed do eiusmod</p></div>
    <h2 class="month-name">AUGUST</h2>
    <div class="event"><span class="day">09</span><p class="details"><strong>Lorem ipsum</strong> dolor sit amet, consectetur adipiscing elit, sed do eiusmod tempor incididunt ut labore et</p></div>
    <div class="event"><span class="day">23</span><p class="details"><strong>Lorem ipsum</strong> dolor sit amet, consectetur adipiscing elit, sed do eiusmod tempor incididunt ut labore et tetur adipiscing elit, sed do eiusmod</p></div>
    <div class="event"><span class="day">31</span><p class="details"><strong>Lorem ipsum</strong> dolor sit amet, consectetur adipiscing elit, sed do eiusmod tempor incididunt ut labore et tetur adipiscing elit, sed do eiusmod</p></div>
  </div>

  <div class="month-column col-3">
    <h2 class="month-name">SEPETEMBER</h2>
    <div class="event"><span class="day">01</span><p class="details"><strong>Lorem ipsum</strong> dolor sit amet, consectetur adipiscing elit, sed do eiusmod tempor incididunt ut labore et</p></div>
    <div class="event"><span class="day">12</span><p class="details"><strong>Lorem ipsum</strong> dolor sit amet, consectetur adipiscing elit, sed do eiusmod tempor incididunt ut labore et tetur adipiscing elit, sed do eiusmod</p></div>
    <div class="event"><span class="day">20</span><p class="details"><strong>Lorem ipsum</strong> dolor sit amet, consectetur adipiscing elit, sed do eiusmod tempor incididunt ut labore et tetur adipiscing elit, sed do eiusmod</p></div>
    <h2 class="month-name">OCTOBER</h2>
    <div class="event"><span class="day">17</span><p class="details"><strong>Lorem ipsum</strong> dolor sit amet, consectetur adipiscing elit, sed do eiusmod tempor incididunt ut labore et</p></div>
    <div class="event"><span class="day">26</span><p class="details"><strong>Lorem ipsum</strong> dolor sit amet, consectetur adipiscing elit, sed do eiusmod tempor incididunt ut labore et tetur adipiscing elit, sed do eiusmod</p></div>
    <h2 class="month-name">NOVEMBER</h2>
    <div class="event"><span class="day">12</span><p class="details"><strong>Lorem ipsum</strong> dolor sit amet, consectetur adipiscing elit, sed do eiusmod tempor incididunt ut labore et</p></div>
    <div class="event"><span class="day">19</span><p class="details"><strong>Lorem ipsum</strong> dolor sit amet, consectetur adipiscing elit, sed do eiusmod tempor incididunt ut labore et tetur adipiscing elit, sed do eiusmod</p></div>
    <div class="event"><span class="day">24</span><p class="details"><strong>Lorem ipsum</strong> dolor sit amet, consectetur adipiscing elit, sed do eiusmod tempor incididunt ut labore et tetur adipiscing elit, sed do eiusmod</p></div>
    <h2 class="month-name">DECEMBER</h2>
    <div class="event"><span class="day">07</span><p class="details"><strong>Lorem ipsum</strong> dolor sit amet, consectetur adipiscing elit, sed do eiusmod tempor incididunt ut labore et</p></div>
    <div class="event"><span class="day">29</span><p class="details"><strong>Lorem ipsum</strong> dolor sit amet, consectetur adipiscing elit, sed do eiusmod tempor incididunt ut labore et tetur adipiscing elit, sed do eiusmod</p></div>
  </div>

  <footer class="sheet-footer">418 Alder Crest Rd NE Suite #200, Riverton OR 97000 Phone: (503) 555-0142 | Fax: (503) 555-0187 | www.tvmassociation.org</footer>
</section>

<section class="reminder-card" aria-label="Event reminder postcard">
  <div class="card-brand">
    <span class="brand-square"></span>
    <span class="brand-name">TVM</span>
  </div>
  <h1 class="card-headline">Register Today<br>for the Feb. 7th<br>TVM Off-the-Clock<br>at Kestrel's Home Center</h1>
  <p class="card-body">Join us for an exciting Off-the-Clock hosted by Kestrel's Home Center on Tuesday, February 7th. Take time after your busy day to relax and meet the appliance experts to discuss your upcoming Tour home or see what's new in the appliance industry. This is not your typical Off-the-Clock as there will be lots of chances to win valuable raffle prizes all while mixing and mingling with your fellow Association members.</p>
  <div class="partner-name">Kestrel's</div>
  <div class="call-line">CALL the TVM (503) 555-0142</div>
  <div class="online-line">or register online</div>
  <div class="web-line">www.tvmassociation.org</div>
  <div class="card-band"></div>
</section>

</body>
</html>
```